New Website for ReBranded Company - CrewBeacon

We have a successful company and website currently but it is a little dated. We have re-branded the company from Harbor Signal Networks to CrewBeacon and have a new logo for the new name. We are looking to build a newer fresher website with the new name. I will need a concept of the home page and one inside page. You can see our current site at https://www.harborsignalnetworks.example and the new site will be https://www.crewbeacon.example .

I also really like the https://www.pathlantern.example/ website. I like ledgerkite.example website. I like the https://skillorbit.example/ website.

See the attached document for layout and some text to use. Use the pictures I attached as opposed to pictures from the old site as much as you can.

Target Market(s)

Business

Industry/Entity Type

Software Service

Number of Pages Required

2 page

Font styles to use
Sans Serif

Requirements
Must have
• Use the colors from my logo. Professional but modern. We want people to feel like our product makes their staff feel safer at work.
Should not have
• Don't use any red or orange (no stop colors).

```html
<!DOCTYPE html>
<html lang="en">
<head>
<meta charset="utf-8">
<title>CrewBeacon</title>
<link href="https://fonts.googleapis.com/css2?family=Montserrat:wght@400;500;600;700;800;900&family=Playfair+Display:wght@400&display=swap" rel="stylesheet">
<style>
:root{
  --blue:#3a8fd0;
  --blue-dark:#2f7fc0;
  --green:#6ab33e;
  --green-dark:#5aa232;
  --ink:#111;
  --text:#333;
  --muted:#666;
  --pale:#eef5fb;
  --line:#e6e6e6;
  --footer:#f4f4f4;
  --bar:#2f2f2f;
}
*{margin:0;padding:0;box-sizing:border-box}
html,body{width:1200px;height:3846px;overflow:hidden}
body{position:relative;background:#fff;font-family:"Montserrat",sans-serif;color:var(--text)}
.abs{position:absolute}
a{color:inherit;text-decoration:none}

/* header */
.site-header{position:absolute;left:0;top:0;width:1200px;height:99px;background:#fff}
.brand{position:absolute;left:142px;top:30px;display:flex;align-items:center;gap:12px}
.brand-dot{width:40px;height:40px;border-radius:50%;background:var(--blue)}
.brand-name{font-size:30px;font-weight:600;color:var(--blue)}
.nav{position:absolute;top:45px;font-size:12px;font-weight:500;color:#222;letter-spacing:.2px}
.btn-solid{position:absolute;background:var(--green);color:#fff;font-size:12px;font-weight:500;display:flex;align-items:center;justify-content:center;text-transform:uppercase}
.btn-outline{position:absolute;border:2px solid var(--blue);border-radius:30px;color:var(--blue);font-size:12.5px;font-weight:600;display:flex;align-items:center;justify-content:center;text-transform:uppercase;letter-spacing:.4px;background:transparent}
.btn-outline .wave{position:absolute;right:-4px;top:-16px}

/* hero */
.hero{position:absolute;left:0;top:99px;width:1200px;height:535px;background:linear-gradient(90deg,#f2f2f0 0%,#e9eaea 40%,#b9c2cc 70%,#7d8a98 100%)}
.hero h1{position:absolute;left:143px;top:120px;font-size:46px;line-height:57px;font-weight:900;color:var(--ink);letter-spacing:-.3px}
.hero p{position:absolute;left:143px;top:298px;font-size:21px;line-height:29px;color:#111;font-weight:500}
.scroll-down{position:absolute;left:580px;top:615px;width:38px;height:38px;border-radius:50%;background:#fff;box-shadow:0 2px 8px rgba(0,0,0,.12);display:flex;align-items:center;justify-content:center}

/* features */
.feature{position:absolute;width:288px;text-align:center;font-size:16.5px;line-height:25px;color:#222}
.feature .shield{display:block;margin:0 auto 24px}
.feature-card{position:absolute;left:455px;top:727px;width:288px;height:295px;background:#fff;box-shadow:0 4px 24px rgba(0,0,0,.07)}

/* alone section */
.alone{position:absolute;left:0;top:1067px;width:1200px;height:582px;background:var(--pale)}
.alone-art{position:absolute;left:142px;top:42px;width:407px;height:470px}
.alone h2{position:absolute;left:630px;top:155px;font-size:28px;line-height:34px;font-weight:700}
.c-blue{color:var(--blue)}.c-green{color:var(--green)}
.divider{position:absolute;height:2px;background:#999}
.checks{position:absolute;left:631px;top:265px;list-style:none;font-size:13.5px;font-weight:600;color:#222}
.checks li{display:flex;align-items:center;gap:12px;height:30px}

/* why */
.section-title{position:absolute;left:0;width:1200px;text-align:center;font-size:28px;font-weight:700}
.why-card{position:absolute;top:1794px;width:288px;height:322px;background:#fff;box-shadow:0 4px 24px rgba(0,0,0,.07);padding:32px 28px}
.why-card h3{position:absolute;left:28px;top:142px;font-size:15px;font-weight:600;color:#222;line-height:22px}
.why-card p,.why-card .opts{position:absolute;left:28px;right:24px;font-size:12px;line-height:20px;color:#444}
.opts ul{list-style:none;columns:2;column-gap:10px}
.opts li::before{content:"•";color:#999;margin-right:7px}

/* split band */
.band{position:absolute;left:0;top:2200px;width:1200px;height:480px}
.band-text{position:absolute;font-size:26px;line-height:34px;font-weight:700;color:#fff;letter-spacing:.3px}
.btn-ghost{position:absolute;border:2px solid #fff;border-radius:30px;color:#fff;font-size:12.5px;font-weight:600;display:flex;align-items:center;justify-content:center;letter-spacing:.5px}
.pill{position:absolute;background:#fff;border-radius:30px;color:#222;font-size:15px;font-weight:700;display:flex;align-items:center;justify-content:center}

/* steps */
.step-circle{position:absolute;width:114px;height:114px;border-radius:50%;background:#fff;box-shadow:0 4px 20px rgba(0,0,0,.08);display:flex;align-items:center;justify-content:center}
.step-num{position:absolute;left:-2px;bottom:-6px;width:22px;height:22px;border-radius:50%;background:#8a8a8a;color:#fff;font-size:11px;font-weight:700;display:flex;align-items:center;justify-content:center}
.step h3{position:absolute;font-size:15px;font-weight:600;color:#222;line-height:22px}
.step ul{position:absolute;list-style:none;font-size:12.5px;color:#444;line-height:26px}
.step ul li::before{content:"•";color:#aaa;margin-right:8px}
.step p{position:absolute;font-size:12.5px;line-height:20.5px;color:#444;width:180px}

/* stay connected */
.stay{position:absolute;left:142px;top:3203px;width:916px;height:140px;background:var(--blue);overflow:hidden}
.stay-photo{position:absolute;left:0;top:0;width:351px;height:140px;background:linear-gradient(90deg,#3d3f44 0%,#6d7278 60%,#9aa3ad 100%)}
.stay h2{position:absolute;left:376px;top:30px;font-family:"Playfair Display",serif;font-weight:400;font-size:33px;color:#fff}
.stay p{position:absolute;left:376px;top:80px;font-size:18px;font-weight:700;color:#fff}

/* footer */
.site-footer{position:absolute;left:0;top:3415px;width:1200px;height:385px;background:var(--footer)}
.footer-about{position:absolute;left:142px;top:167px;width:290px;font-size:12px;line-height:23px;color:#222}
.footer-call{position:absolute;left:142px;top:292px;font-size:15px;font-weight:700;color:#111}
.footer-col{position:absolute;top:82px}
.footer-col h4{font-size:15px;font-weight:600;color:var(--blue);margin-bottom:12px}
.footer-col .mark{width:12px;height:12px;border-radius:50%;border:2px solid var(--green);margin-bottom:10px}
.footer-col ul{list-style:none;font-size:12.5px;line-height:28px;color:#333}
.footer-col li::before{content:"»";color:#777;margin-right:9px}
.bottom-bar{position:absolute;left:0;top:3800px;width:1200px;height:46px;background:var(--bar)}
.bottom-bar small{position:absolute;left:142px;top:16px;font-size:12px;color:#eee}
.social{position:absolute;top:10px;width:26px;height:26px;border-radius:50%}
</style>
</head>
<body>

<header class="site-header">
  <div class="brand"><span class="brand-dot"></span><span class="brand-name">CrewBeacon</span></div>
  <a class="nav" style="left:546px">HOME</a>
  <a class="nav" style="left:618px">BUY ADDONS</a>
  <a class="nav" style="left:734px">CUSTOMER LOGIN</a>
  <a class="btn-solid" style="left:879px;top:34px;width:179px;height:36px">Explore Your Choices</a>
</header>

<section class="hero">
  <div class="abs" role="img" aria-label="Smiling office worker wearing a panic button pendant, colleagues meeting behind her" style="left:600px;top:0;width:600px;height:535px;background:linear-gradient(90deg,rgba(255,255,255,0) 0%,rgba(70,85,110,.35) 100%)"></div>
  <h1>FEEL CONFIDENT<br>THAT YOUR STAFF<br>IS PROTECTED</h1>
  <p>Get A Revolutionary New Electronic<br>Panic Button</p>
  <a class="btn-solid" style="left:142px;top:374px;width:177px;height:34px">Ready To Get Started</a>
  <div class="scroll-down"><svg width="14" height="9" viewBox="0 0 14 9"><path d="M1 1l6 6 6-6" fill="none" stroke="#6ab33e" stroke-width="2"/></svg></div>
</section>

<!-- features -->
<div class="feature-card"></div>
<div class="feature" style="left:141px;top:754px">
  <svg class="shield" width="126" height="140" viewBox="0 0 126 140"><path d="M63 4 L120 30 V82 C120 110 90 130 63 136 C36 130 6 110 6 82 V30 Z" fill="#fff" stroke="#e3e3e3" stroke-width="4"/><g fill="none" stroke="#3a8fd0" stroke-width="2"><rect x="48" y="44" width="14" height="14" rx="3"/><circle cx="74" cy="62" r="6"/><path d="M55 58v8h-20v10M55 66h20v10M55 66v10"/></g><g fill="none" stroke="#6ab33e" stroke-width="2"><circle cx="35" cy="82" r="4"/><circle cx="55" cy="82" r="4"/><circle cx="75" cy="82" r="4"/><circle cx="92" cy="82" r="4"/></g></svg>
  Problems Stopped Before<br>They Start For Any Type of<br>Organization
</div>
<div class="feature" style="left:455px;top:754px">
  <svg class="shield" width="126" height="140" viewBox="0 0 126 140"><path d="M63 4 L120 30 V82 C120 110 90 130 63 136 C36 130 6 110 6 82 V30 Z" fill="#fff" stroke="#e3e3e3" stroke-width="4"/><circle cx="66" cy="60" r="15" fill="none" stroke="#6ab33e" stroke-width="2.5"/><text x="66" y="66" text-anchor="middle" font-family="Montserrat,sans-serif" font-size="17" font-weight="700" fill="#6ab33e">$</text><path d="M36 86 h14 l10 6 h20 l14 -8" fill="none" stroke="#3a8fd0" stroke-width="2.5"/></svg>
  Affordable Prices Starting at $18<br>per month. No Contracts. No<br>Hidden Costs
</div>
<div class="feature" style="left:769px;top:754px">
  <svg class="shield" width="126" height="140" viewBox="0 0 126 140"><path d="M63 4 L120 30 V82 C120 110 90 130 63 136 C36 130 6 110 6 82 V30 Z" fill="#fff" stroke="#e3e3e3" stroke-width="4"/><rect x="54" y="52" width="36" height="26" rx="2" fill="none" stroke="#3a8fd0" stroke-width="2"/><rect x="74" y="56" width="11" height="8" fill="#6ab33e"/><path d="M66 78v6h12" stroke="#3a8fd0" stroke-width="2" fill="none"/><rect x="36" y="66" width="12" height="20" rx="2" fill="none" stroke="#6ab33e" stroke-width="2"/><path d="M42 44v18M42 44h14" stroke="#3a8fd0" stroke-width="1.5" stroke-dasharray="3 2" fill="none"/></svg>
  Alerts by computer, mobile<br>device, text, phone, email,<br>monitoring and E911
</div>

<!-- alone -->
<section class="alone">
  <div class="alone-art" role="img" aria-label="Large shield illustration with signal waves and staff figures" style="background:linear-gradient(160deg,#5fa6dc 0%,#3a8fd0 70%,#2f7fc0 100%);border-radius:40px 40px 200px 200px;opacity:.9"></div>
  <h2><span class="c-blue">Your empoyees shouldn’t feel</span><br><span class="c-green">alone when they need help</span></h2>
  <div class="divider" style="left:631px;top:236px;width:52px"></div>
  <ul class="checks">
    <li><svg width="14" height="14" viewBox="0 0 14 14"><rect x="1" y="1" width="12" height="12" rx="2" fill="none" stroke="#3a8fd0" stroke-width="1.6"/><path d="M4 7l2.2 2.2L11 4" fill="none" stroke="#3a8fd0" stroke-width="1.8"/></svg>Does this problem make you feel frustrated and anxious?</li>
    <li><svg width="14" height="14" viewBox="0 0 14 14"><rect x="1" y="1" width="12" height="12" rx="2" fill="none" stroke="#3a8fd0" stroke-width="1.6"/><path d="M4 7l2.2 2.2L11 4" fill="none" stroke="#3a8fd0" stroke-width="1.8"/></svg>Put a simple solution in their hands</li>
  </ul>
  <a class="btn-outline" style="left:631px;top:355px;width:204px;height:36px">Ready To Get Started<svg class="wave" width="26" height="18" viewBox="0 0 26 18"><g fill="none" stroke="#6ab33e" stroke-width="2.2"><path d="M2 3a20 20 0 0 1 22 12"/><path d="M2 8a13 13 0 0 1 15 8"/><path d="M2 13a6 6 0 0 1 7 4"/></g></svg></a>
</section>

<!-- why -->
<h2 class="section-title" style="top:1714px"><span class="c-blue">Why Businesses</span> <span class="c-green">Choose Us</span></h2>
<div class="divider" style="left:574px;top:1763px;width:52px;background:#aaa"></div>

<div class="why-card" style="left:142px">
  <svg width="80" height="76" viewBox="0 0 80 76"><circle cx="52" cy="40" r="28" fill="#eef5fb"/><rect x="3" y="3" width="30" height="14" rx="2" fill="none" stroke="#6ab33e" stroke-width="2.5"/><path d="M14 12v34l-6-6-4 4 14 18h22l4-22-18-4V12a4 4 0 0 0-8 0z" fill="#fff" stroke="#3a8fd0" stroke-width="2.5"/></svg>
  <h3>Easy To Use</h3>
  <p style="top:170px">Press a button and let the right people know you need help and open a chat window letting everyone talk on resolving their problem.</p>
</div>
<div class="why-card" style="left:455px">
  <svg width="80" height="76" viewBox="0 0 80 76"><circle cx="52" cy="40" r="28" fill="#eef5fb"/><path d="M40 20a24 20 0 1 1 16 28l4 10-14-8" fill="#fff" stroke="#6ab33e" stroke-width="2.5"/><path d="M28 10a24 20 0 1 0 0 40l-10 8 4-12a22 20 0 0 1 6-36z" fill="#fff" stroke="#3a8fd0" stroke-width="2.5"/><path d="M18 24h20M18 32h20M18 40h14" stroke="#3a8fd0" stroke-width="2.2"/></svg>
  <h3 style="top:134px">Communicate The Way<br>You Want</h3>
  <div class="opts" style="top:184px">We give you lots of options:
    <ul style="margin-top:8px;line-height:21.5px"><li>Computer</li><li>Mobile</li><li>Email</li><li>Phone call</li><li>Text</li><li>E911</li><li>Call Center</li></ul>
  </div>
</div>
<div class="why-card" style="left:770px">
  <svg width="80" height="76" viewBox="0 0 80 76"><circle cx="52" cy="40" r="28" fill="#eef5fb"/><rect x="6" y="6" width="34" height="46" fill="#fff" stroke="#3a8fd0" stroke-width="2.5"/><text x="23" y="28" text-anchor="middle" font-family="Montserrat,sans-serif" font-size="16" font-weight="700" fill="#3a8fd0">$</text><path d="M12 36h22M12 43h16" stroke="#3a8fd0" stroke-width="2.2"/><path d="M50 36l14 6v10c0 8-7 12-14 14-7-2-14-6-14-14V42z" fill="#fff" stroke="#6ab33e" stroke-width="2.5"/><path d="M44 51l5 5 8-9" fill="none" stroke="#6ab33e" stroke-width="2.5"/></svg>
  <h3>Cost Effective Protection</h3>
  <p style="top:170px">By leveraging your existing network and equipment we can lower your costs to give better options to your staff.</p>
</div>
<a class="btn-outline" style="left:494px;top:2166px;width:204px;height:36px">Ready To Get Started<svg class="wave" width="26" height="18" viewBox="0 0 26 18"><g fill="none" stroke="#6ab33e" stroke-width="2.2"><path d="M2 3a20 20 0 0 1 22 12"/><path d="M2 8a13 13 0 0 1 15 8"/><path d="M2 13a6 6 0 0 1 7 4"/></g></svg></a>

<!-- split band -->
<svg class="band" width="1200" height="480" viewBox="0 0 1200 480" role="img" aria-label="Split band with photos of an office desk phone tinted blue and green">
  <polygon points="0,9 601,84 1200,12 1200,470 601,412 0,410" fill="#8a8a8a"/>
  <polygon points="0,22 601,90 601,405 0,398" fill="#3f8fcf"/>
  <polygon points="601,90 1200,24 1200,460 601,405" fill="#72b545"/>
  <polygon points="0,22 601,90 601,405 0,398" fill="url(#bg1)"/>
  <polygon points="601,90 1200,24 1200,460 601,405" fill="url(#bg2)"/>
  <defs>
    <linearGradient id="bg1" x1="0" y1="0" x2="1" y2="1"><stop offset="0" stop-color="#5aa0d8" stop-opacity=".4"/><stop offset="1" stop-color="#2a6fa8" stop-opacity=".5"/></linearGradient>
    <linearGradient id="bg2" x1="0" y1="0" x2="1" y2="1"><stop offset="0" stop-color="#86c45e" stop-opacity=".3"/><stop offset="1" stop-color="#4f8c2a" stop-opacity=".45"/></linearGradient>
  </defs>
</svg>
<div class="band-text" style="left:143px;top:2346px">We know how scary it<br>can feel to worry about<br>employee safety.</div>
<a class="btn-ghost" style="left:143px;top:2488px;width:170px;height:36px">START MY DEMO</a>
<div class="band-text" style="right:100px;top:2346px;text-align:right">That’s why we have provided<br>a way for customers to get<br>help to staff effectively in</div>
<div class="pill" style="left:721px;top:2479px;width:188px;height:37px">45 States covering</div>
<div class="pill" style="left:925px;top:2479px;width:133px;height:37px">5 Countries</div>

<!-- steps -->
<h2 class="section-title" style="top:2687px"><span class="c-blue">Simple</span> <span class="c-green">Start Plan</span></h2>
<div class="divider" style="left:574px;top:2738px;width:52px;background:#aaa"></div>

<div class="step">
  <div class="step-circle" style="left:200px;top:2764px"><svg width="58" height="56" viewBox="0 0 58 56"><rect x="8" y="4" width="42" height="48" rx="4" fill="none" stroke="#3a8fd0" stroke-width="3"/><path d="M16 18h26M16 28h26M16 38h18" stroke="#6ab33e" stroke-width="3"/></svg><span class="step-num">1</span></div>
  <h3 style="left:200px;top:2896px">Explore Your Choices</h3>
  <ul style="left:200px;top:2924px"><li>Pricing</li><li>Trial</li><li>Quote</li><li>Hardware</li></ul>
</div>
<svg class="abs" style="left:362px;top:2806px" width="130" height="40" viewBox="0 0 130 40"><path d="M2 26 C40 0 90 4 122 28" fill="none" stroke="#999" stroke-dasharray="4 4" stroke-width="1.4"/><path d="M114 22l8 6-9 3" fill="none" stroke="#999" stroke-width="1.4"/></svg>
<div class="step">
  <div class="step-circle" style="left:543px;top:2764px"><svg width="58" height="58" viewBox="0 0 58 58"><rect x="5" y="5" width="48" height="48" rx="6" fill="none" stroke="#3a8fd0" stroke-width="3"/><circle cx="29" cy="29" r="9" fill="none" stroke="#6ab33e" stroke-width="3"/><circle cx="29" cy="29" r="15" fill="none" stroke="#6ab33e" stroke-width="3" stroke-dasharray="5 4"/></svg><span class="step-num">2</span></div>
  <h3 style="left:543px;top:2896px">Get Setup</h3>
  <ul style="left:543px;top:2924px"><li>Input Your Alerts</li><li>Input Your Staff</li><li>Install Our Software</li></ul>
</div>
<svg class="abs" style="left:705px;top:2806px" width="130" height="40" viewBox="0 0 130 40"><path d="M2 14 C40 40 90 36 122 10" fill="none" stroke="#999" stroke-dasharray="4 4" stroke-width="1.4"/><path d="M112 9l10 1-3 9" fill="none" stroke="#999" stroke-width="1.4"/></svg>
<div class="step">
  <div class="step-circle" style="left:883px;top:2764px"><svg width="60" height="58" viewBox="0 0 60 58"><circle cx="30" cy="14" r="10" fill="none" stroke="#6ab33e" stroke-width="2.5"/><path d="M30 6v16M22 14h16" stroke="#6ab33e" stroke-width="2"/><circle cx="16" cy="34" r="6" fill="none" stroke="#3a8fd0" stroke-width="2.5"/><circle cx="44" cy="34" r="6" fill="none" stroke="#3a8fd0" stroke-width="2.5"/><path d="M4 54c0-8 6-12 12-12s12 4 12 12M32 54c0-8 6-12 12-12s12 4 12 12" fill="none" stroke="#3a8fd0" stroke-width="2.5"/></svg><span class="step-num">3</span></div>
  <h3 style="left:884px;top:2896px">Feel Confident Your<br>Staff Is Protected</h3>
  <p style="left:884px;top:2950px">High Five. You just too a major step to getting rid of the anxiety and frustration this gave you.</p>
</div>
<a class="btn-outline" style="left:513px;top:3072px;width:168px;height:37px">Start My Demo<svg class="wave" width="26" height="18" viewBox="0 0 26 18"><g fill="none" stroke="#6ab33e" stroke-width="2.2"><path d="M2 3a20 20 0 0 1 22 12"/><path d="M2 8a13 13 0 0 1 15 8"/><path d="M2 13a6 6 0 0 1 7 4"/></g></svg></a>

<!-- stay connected -->
<section class="stay">
  <div class="stay-photo" role="img" aria-label="Office desk phone beside a panic button device"></div>
  <h2>Stay Connected</h2>
  <p>Swith Staff during a Crisis Situations</p>
  <a class="btn-solid" style="left:745px;top:55px;width:126px;height:36px;font-size:12px;font-weight:600;text-transform:none">Start My Demo</a>
</section>

<!-- footer -->
<footer class="site-footer">
  <div class="brand" style="top:88px"><span class="brand-dot"></span><span class="brand-name">CrewBeacon</span></div>
  <p class="footer-about">When employees feel alone during a<br>threatening situation, we give them a<br>way to let the right resources know that<br>they need help so you can feel confident<br>that your staff is protected.</p>
  <div class="footer-call">CALL US1–800–555-0148</div>
  <div class="footer-col" style="left:452px"><h4>Shop</h4><div class="mark"></div><ul><li>Add Ons</li><li>Start My</li><li>Demo</li><li>Custom Quote</li><li>Start Trial</li></ul></div>
  <div class="footer-col" style="left:652px"><h4>About</h4><div class="mark"></div><ul><li>Affiliates</li><li>Contact</li><li>Support</li><li>Existing Customers</li><li>Industries</li><li>Blog</li><li>FAQ</li></ul></div>
  <div class="footer-col" style="left:870px"><h4>Legal</h4><div class="mark"></div><ul><li>Privacy Policy</li><li>Terms of Use</li><li>End User License Agreement</li></ul></div>
</footer>
<div class="bottom-bar">
  <small>Copyright © 2020 CrewBeacon. All Rights Reserved.</small>
  <span class="social" style="left:926px;background:var(--green)"></span>
  <span class="social" style="left:961px;border:2px solid #fff"></span>
  <span class="social" style="left:996px;border:2px solid #fff"></span>
  <span class="social" style="left:1031px;border:2px solid #fff"></span>
</div>

</body>
</html>
```